[WEB DESIGN - Start-up] Online LOANS against Luxury Assets - Needs a Web Design

Hello,
We need a web design for a new company. We make online LOANS against Luxury assets.
The name is private, that's why you could remplace it by the term "LOGO" or "ENTERPRISE".

In attachments, you'll find few models that we would like. Nonetheless, we don't want a copy of these screenshots. They are only prototypes that we made. Here we expect you to lead a professional web Design with your intuition and your ideas.

The final design should communicate start-up spirit, professionalism and fluidity.

Best Regards.

Industry/Entity Type

Finance

Number of Pages Required

2 page

Font styles to use
Sans Serif

Colors
f78f20
ffffff
b2b2b2
e9e9e9

Requirements
Must have
• The designer will draw on the 2015 web trends.
• The subject site is serious (loans against luxury assets), but the site should be modern and pleasant.
• PLEASE REFER YOU TO MY MODEL ( ATTACHMENTS)
Nice to have
• Surprise-me ! Welcome to a lot of imagination.

```html
<!DOCTYPE html>
<html lang="fr">
<head>
<meta charset="utf-8">
<title>Entreprise — Prêts sur biens de luxe</title>
<link rel="stylesheet" href="https://fonts.googleapis.com/css2?family=Open+Sans:wght@400;600;700;800&display=swap">
<style>
:root{
  --orange:#f78f20;
  --orange-dark:#e07a10;
  --white:#ffffff;
  --grey:#b2b2b2;
  --light:#e9e9e9;
  --ink:#333333;
  --text:#6b6b6b;
  --dark:#24262a;
  --darker:#1b1c1f;
}
*{box-sizing:border-box;margin:0;padding:0}
html,body{width:1200px;height:2236px;overflow:hidden}
body{font-family:"Open Sans",Arial,sans-serif;color:var(--ink);background:var(--white);position:relative}
.abs{position:absolute}

/* header */
.site-header{position:absolute;left:0;top:0;width:1200px;height:88px;background:var(--white);box-shadow:0 2px 6px rgba(0,0,0,.08);z-index:2}
.logo{position:absolute;left:160px;top:22px;font-size:34px;font-weight:800;color:var(--orange);letter-spacing:1px}
.main-nav{position:absolute;left:378px;top:0;display:flex;height:88px}
.main-nav a{display:block;padding:0 18px;line-height:42px;font-size:13px;color:var(--ink);text-decoration:none;font-weight:600}
.main-nav a.active{background:var(--orange);color:var(--white);height:42px}
.header-phone{position:absolute;left:930px;top:10px;display:flex;align-items:center;gap:8px;font-size:20px;font-weight:700;color:var(--orange)}

/* hero */
.hero{position:absolute;left:0;top:88px;width:1200px;height:344px;background:radial-gradient(circle at 70% 45%,#6b5a48 0%,#3b342e 40%,#1d1c1c 100%);overflow:hidden}
.hero-visual{position:absolute;inset:0;background:radial-gradient(circle at 85% 30%,rgba(247,143,32,.35),transparent 35%),radial-gradient(circle at 55% 80%,rgba(200,170,130,.25),transparent 40%)}
.hero-arrow{position:absolute;top:150px;font-size:40px;color:var(--white);font-weight:300}
.search-box{position:absolute;left:160px;top:8px;width:272px;height:266px;background:var(--white);box-shadow:0 4px 14px rgba(0,0,0,.35)}
.search-head{background:var(--orange);color:var(--white);font-size:15px;padding:9px 14px;font-weight:400}
.search-head b{font-weight:800}
.search-body{padding:12px 14px}
.search-label{font-size:11px;font-weight:700;color:var(--ink);margin-bottom:8px}
.field{height:30px;border:1px solid #d6d6d6;margin-bottom:10px;font-size:10px;color:var(--grey);padding:8px 10px;display:flex;align-items:center;gap:6px}
.field i{display:inline-block;width:9px;height:9px;border-radius:50%;background:var(--grey)}
.search-btn{display:block;margin:6px auto 0;width:180px;height:32px;background:#2b2b2b;color:var(--white);font-size:12px;font-weight:700;text-align:center;line-height:32px;letter-spacing:.5px}
.hero-title{position:absolute;left:470px;top:100px;color:var(--white);font-size:40px;font-weight:800;line-height:50px;letter-spacing:1px;text-shadow:0 2px 6px rgba(0,0,0,.4)}
.hero-title mark{background:var(--orange);color:var(--white);padding:0 8px}

/* common */
.section-title{position:absolute;left:0;width:1200px;text-align:center;font-size:26px;font-weight:800;color:var(--ink);text-transform:uppercase;letter-spacing:.5px}
.section-title::after{content:"";display:block;width:50px;height:3px;background:var(--orange);margin:10px auto 0}

/* steps */
.step{position:absolute;top:548px;width:200px;text-align:center}
.step svg{display:block;margin:0 auto}
.step h3{font-size:13px;font-weight:800;color:var(--ink);margin-top:12px}
.step p{font-size:11px;line-height:16px;color:var(--text);margin-top:8px}

/* assets */
.assets{position:absolute;left:0;top:760px;width:1200px;height:540px;background:var(--light)}
.asset{position:absolute;width:204px}
.asset-img{height:184px;display:flex;align-items:center;justify-content:center;color:var(--white);font-size:13px;font-weight:700}
.asset-name{font-size:13px;text-align:center;color:var(--ink);margin-top:8px;font-weight:600}

/* help */
.help-item{position:absolute;top:1420px;width:240px;text-align:center}
.help-circle{width:96px;height:96px;border-radius:50%;margin:0 auto;display:flex;align-items:center;justify-content:center;border:3px solid var(--orange);background:var(--white)}
.help-circle.filled{background:var(--orange)}
.help-item h3{font-size:13px;font-weight:600;color:var(--ink);margin-top:14px}
.help-item p{font-size:14px;font-weight:700;color:var(--orange);margin-top:4px}

/* proof band */
.proof{position:absolute;left:0;top:1600px;width:1200px;height:420px;background:linear-gradient(180deg,#34373c,#26282c)}
.proof-title{position:absolute;top:26px;left:0;width:1200px;text-align:center;color:var(--white);font-size:26px;font-weight:800;text-transform:uppercase}
.panel-head{position:absolute;top:88px;color:var(--white);font-size:14px;font-weight:600;display:flex;align-items:center;gap:8px}
.panel-head span.dot{width:18px;height:18px;background:var(--orange);border-radius:3px}
.testimonials{position:absolute;left:160px;top:118px;width:420px;height:266px;background:var(--orange);padding:16px}
.quote{display:flex;gap:10px;margin-bottom:10px;align-items:flex-start}
.quote .bubble{flex:1;background:var(--white);padding:9px 12px;font-size:10px;line-height:14px;color:var(--text);border-radius:3px}
.quote .bubble b{display:block;color:var(--ink);font-size:10px}
.avatar{width:42px;height:42px;border-radius:50%;background:#d9d9d9;border:2px solid var(--white);flex:none}
.figures{position:absolute;left:632px;top:118px;width:420px;height:266px;background:#3e4146}
.figures-top{background:var(--orange);height:150px;padding:12px 16px;text-align:center;color:var(--white)}
.figures-top h4{font-size:12px;font-weight:700}
.counter{display:flex;justify-content:center;gap:6px;margin-top:14px}
.counter span{width:28px;height:40px;background:var(--white);color:var(--ink);font-size:24px;font-weight:800;line-height:40px;text-align:center;border-radius:2px}
.counter span.sep{background:none;width:6px;color:var(--white)}
.counter-labels{display:flex;justify-content:center;gap:40px;margin-top:6px;font-size:9px}
.figures-photo{height:116px;background:linear-gradient(120deg,#5a5d62,#2f3236);padding:18px;color:var(--white);text-align:center}
.figures-photo p{font-size:11px;line-height:16px}
.figures-photo a{display:inline-block;margin-top:10px;background:var(--orange);color:var(--white);font-size:11px;font-weight:700;padding:7px 20px;text-decoration:none}

/* footer */
.site-footer{position:absolute;left:0;top:2020px;width:1200px;height:216px;background:var(--darker)}
.foot-col{position:absolute;top:28px}
.foot-col h5{font-size:12px;font-weight:700;color:var(--white);margin-bottom:12px;letter-spacing:.5px}
.foot-col p,.foot-col li{font-size:10px;line-height:17px;color:#9a9a9a;list-style:none}
.foot-col li::before{content:"› ";color:var(--orange)}
.foot-col .orange{color:var(--orange)}
.news-input{width:190px;height:28px;background:#2e3034;margin-top:8px;font-size:10px;color:#888;padding:7px 10px}
.news-btn{display:inline-block;margin-top:8px;background:var(--orange);color:var(--white);font-size:10px;font-weight:700;padding:6px 16px}
</style>
</head>
<body>

<header class="site-header">
  <div class="logo">LOGO</div>
  <nav class="main-nav">
    <a class="active" href="#">Accueil</a>
    <a href="#">Les Biens</a>
    <a href="#">Estimation</a>
    <a href="#">Faq</a>
    <a href="#">Mon Compte</a>
  </nav>
  <div class="header-phone">
    <svg width="22" height="22" viewBox="0 0 24 24"><path fill="#f78f20" d="M6.6 10.8a15 15 0 0 0 6.6 6.6l2.2-2.2c.3-.3.7-.4 1-.2 1.1.4 2.3.6 3.6.6.6 0 1 .4 1 1V20c0 .6-.4 1-1 1A17 17 0 0 1 3 4c0-.6.4-1 1-1h3.5c.6 0 1 .4 1 1 0 1.3.2 2.5.6 3.6.1.3 0 .7-.2 1z"/></svg>
    01 23 45 67 89
  </div>
</header>

<section class="hero">
  <div class="hero-visual" role="img" aria-label="Photo d'une montre de luxe en gros plan, tons bruns et dorés"></div>
  <div class="hero-arrow" style="left:90px">‹</div>
  <div class="hero-arrow" style="left:1090px">›</div>
  <form class="search-box">
    <div class="search-head"><b>Nature</b> De l'Objet</div>
    <div class="search-body">
      <div class="search-label">Vérifiez une requête</div>
      <div class="field"><i></i>Type de bien</div>
      <div class="field"><i></i>Marque ou modèle</div>
      <div class="field"><i></i>Valeur estimée</div>
      <div class="search-btn">RECHERCHER</div>
    </div>
  </form>
  <h1 class="hero-title">ON SE <mark>PRÊTE</mark> DE TOUT<br>SAUF DE L'ARGENT</h1>
</section>

<h2 class="section-title" style="top:478px">Comment ça fonctionne</h2>

<div class="step" style="left:160px">
  <svg width="56" height="50" viewBox="0 0 56 50"><circle cx="20" cy="28" r="18" fill="#f78f20"/><circle cx="38" cy="20" r="16" fill="none" stroke="#f78f20" stroke-width="3"/><text x="20" y="35" font-size="20" font-weight="800" fill="#fff" text-anchor="middle" font-family="Open Sans,sans-serif">$</text></svg>
  <h3>ESTIMATION</h3>
  <p>Décrivez votre bien en ligne et recevez une première estimation gratuite sous vingt-quatre heures.</p>
</div>
<div class="step" style="left:380px">
  <svg width="56" height="50" viewBox="0 0 56 50"><rect x="6" y="10" width="44" height="30" rx="3" fill="#f78f20"/><path d="M6 13l22 16 22-16" fill="none" stroke="#fff" stroke-width="3"/></svg>
  <h3>PAIEMENT</h3>
  <p>Après validation de l'expertise, les fonds sont versés directement sur votre compte bancaire.</p>
</div>
<div class="step" style="left:600px">
  <svg width="56" height="50" viewBox="0 0 56 50"><path d="M28 4l20 8v12c0 12-9 20-20 24C17 44 8 36 8 24V12z" fill="#f78f20"/><path d="M19 25l7 7 12-13" fill="none" stroke="#fff" stroke-width="4"/></svg>
  <h3>SECURISATION</h3>
  <p>Votre bien est conservé dans un coffre assuré et surveillé pendant toute la durée du prêt.</p>
</div>
<div class="step" style="left:820px">
  <svg width="56" height="50" viewBox="0 0 56 50"><path d="M6 10h34a8 8 0 0 1 8 8v10a8 8 0 0 1-8 8H22l-10 9v-9H6z" fill="#f78f20"/><circle cx="18" cy="23" r="3" fill="#fff"/><circle cx="28" cy="23" r="3" fill="#fff"/><circle cx="38" cy="23" r="3" fill="#fff"/></svg>
  <h3>RACHAT</h3>
  <p>Remboursez votre prêt à tout moment et récupérez votre objet dans son état d'origine.</p>
</div>

<section class="assets">
  <h2 class="section-title" style="top:20px">Les biens que nous acceptons</h2>

  <div class="asset" style="left:168px;top:66px"><div class="asset-img" role="img" aria-label="Photo de pierres précieuses" style="background:linear-gradient(135deg,#2c2f36,#7c8088)"></div><div class="asset-name">Pierres Précieuses</div></div>
  <div class="asset" style="left:388px;top:66px"><div class="asset-img" role="img" aria-label="Photo d'un véhicule de luxe" style="background:linear-gradient(135deg,#c56e1a,#f0a04a)">Véhicules</div><div class="asset-name">&nbsp;</div></div>
  <div class="asset" style="left:608px;top:66px"><div class="asset-img" role="img" aria-label="Photo d'un sac de luxe" style="background:linear-gradient(135deg,#1d1d1f,#5a4a3e)"></div><div class="asset-name">Sacs De Luxe</div></div>
  <div class="asset" style="left:828px;top:66px"><div class="asset-img" role="img" aria-label="Photo de lingots d'or" style="background:linear-gradient(135deg,#3a2a12,#c9962f)"></div><div class="asset-name">Métaux Précieux</div></div>

  <div class="asset" style="left:168px;top:294px"><div class="asset-img" role="img" aria-label="Photo d'une montre dorée" style="background:linear-gradient(135deg,#2a2621,#a98a52)"></div><div class="asset-name">Montres</div></div>
  <div class="asset" style="left:388px;top:294px"><div class="asset-img" role="img" aria-label="Photo de bouteilles de vin" style="background:linear-gradient(135deg,#b8621a,#3c1d10)"></div><div class="asset-name">Vins &amp; Spiritueux</div></div>
  <div class="asset" style="left:608px;top:294px"><div class="asset-img" role="img" aria-label="Photo d'articles de maroquinerie" style="background:linear-gradient(135deg,#1e3a5c,#6c4a34)"></div><div class="asset-name">Maroquinerie</div></div>
  <div class="asset" style="left:828px;top:294px"><div class="asset-img" role="img" aria-label="Photo de bouteilles de spiritueux" style="background:linear-gradient(135deg,#d07a22,#5a2c10)"></div><div class="asset-name">Vins &amp; Spiritueux</div></div>
</section>

<h2 class="section-title" style="top:1334px">Besoin d'aide ? Nous sommes à votre écoute</h2>

<div class="help-item" style="left:180px">
  <div class="help-circle"><svg width="40" height="40" viewBox="0 0 24 24"><path fill="#f78f20" d="M6.6 10.8a15 15 0 0 0 6.6 6.6l2.2-2.2c.3-.3.7-.4 1-.2 1.1.4 2.3.6 3.6.6.6 0 1 .4 1 1V20c0 .6-.4 1-1 1A17 17 0 0 1 3 4c0-.6.4-1 1-1h3.5c.6 0 1 .4 1 1 0 1.3.2 2.5.6 3.6.1.3 0 .7-.2 1z"/></svg></div>
  <h3>Call Us</h3>
  <p>01 23 45 67 89</p>
</div>
<div class="help-item" style="left:480px">
  <div class="help-circle filled"><svg width="40" height="40" viewBox="0 0 40 40"><text x="20" y="31" font-size="32" font-weight="800" fill="#fff" text-anchor="middle" font-family="Open Sans,sans-serif">?</text></svg></div>
  <h3>Questions Fréquentes</h3>
</div>
<div class="help-item" style="left:760px">
  <div class="help-circle"><svg width="40" height="32" viewBox="0 0 40 32"><rect x="3" y="4" width="34" height="24" rx="2" fill="none" stroke="#f78f20" stroke-width="3"/><path d="M3 6l17 13 17-13" fill="none" stroke="#f78f20" stroke-width="3"/></svg></div>
  <h3>Formulaire De Contact</h3>
  <p style="font-size:11px">contact@pretluxe-exemple.fr</p>
</div>

<section class="proof">
  <h2 class="proof-title">Entreprise est n°1 de la vente avec faculté de rachat</h2>

  <div class="panel-head" style="left:160px"><span class="dot"></span>Derniers Témoignages</div>
  <div class="testimonials">
    <div class="quote"><div class="avatar" role="img" aria-label="Portrait d'un client"></div><div class="bubble"><b>Marc D.</b>Service rapide et très professionnel, j'ai obtenu mon prêt en deux jours seulement.</div></div>
    <div class="quote"><div class="bubble"><b>Sophie L.</b>Une équipe à l'écoute, une estimation juste et un suivi impeccable du début à la fin.</div><div class="avatar" role="img" aria-label="Portrait d'une cliente"></div></div>
    <div class="quote"><div class="avatar" role="img" aria-label="Portrait d'un client"></div><div class="bubble"><b>Julien R.</b>J'ai récupéré ma montre en parfait état après le remboursement. Je recommande.</div></div>
  </div>

  <div class="panel-head" style="left:632px"><span class="dot"></span>Quelques chiffres</div>
  <div class="figures">
    <div class="figures-top">
      <h4>Nous, ayez confiance en nos résultats</h4>
      <div class="counter"><span>0</span><span>2</span><span>8</span><span class="sep">|</span><span>1</span><span>5</span><span class="sep">|</span><span>4</span><span>5</span><span class="sep">|</span><span>0</span><span>5</span></div>
      <div class="counter-labels"><span>Prêts</span><span>Clients</span><span>Biens</span><span>Années</span></div>
    </div>
    <div class="figures-photo" role="img" aria-label="Photo d'ambiance d'un bureau d'expertise">
      <p>Des milliers de clients nous font confiance chaque année pour financer leurs projets.</p>
      <a href="#">EN SAVOIR PLUS</a>
    </div>
  </div>
</section>

<footer class="site-footer">
  <div class="foot-col" style="left:160px;width:220px">
    <h5>ABOUT US</h5>
    <p>Nous proposons des prêts rapides garantis par vos biens de luxe, avec une expertise transparente et un stockage sécurisé.</p>
    <p class="orange" style="margin-top:8px">Read More</p>
  </div>
  <div class="foot-col" style="left:420px">
    <h5>INFO MENU</h5>
    <ul><li>Accueil</li><li>Les Biens</li><li>Estimation</li><li>Faq</li><li>Mon Compte</li></ul>
  </div>
  <div class="foot-col" style="left:640px;width:200px">
    <h5>CONTACT US</h5>
    <p>12 rue de l'Exemple<br>75000 Paris, France</p>
    <p class="orange" style="font-weight:700;margin-top:6px">01 23 45 67 89</p>
    <p>contact@pretluxe-exemple.fr</p>
  </div>
  <div class="foot-col" style="left:870px">
    <h5>GET IN TOUCH</h5>
    <p>Inscrivez-vous à notre newsletter.</p>
    <div class="news-input">Votre adresse email</div>
    <div class="news-btn">ENVOYER</div>
  </div>
</footer>

</body>
</html>
```